Business Cards and Print Material
Business cards and print material
I like something that is out of the box. Something different and memorable. I will also need design for envelopes and letter heads. I like the designs so far. Please keep up the good work!
any info or ideas on what you would like ????

```html
<!DOCTYPE html>
<html lang="en">
<head>
<meta charset="utf-8">
<title>Alder Grove Imaging – Stationery Set</title>
<link rel="stylesheet" href="https://fonts.googleapis.com/css2?family=Open+Sans:wght@400;600&display=swap">
<style>
  :root {
    --backdrop: #e3e3e3;
    --backdrop-edge: #d2d2d2;
    --paper: #ffffff;
    --paper-line: #c9c9c9;
    --navy: #2e2b5f;
    --brand: #5d62a0;
    --muted: #6d6f86;
    --figure-a: #dfe3f1;
    --figure-b: #8f9ccc;
  }
  * { box-sizing: border-box; margin: 0; padding: 0; }
  html, body { width: 1200px; height: 869px; overflow: hidden; }
  body {
    background: var(--backdrop);
    font-family: "Open Sans", Arial, sans-serif;
    position: relative;
  }
  .stage {
    position: absolute; left: 10px; top: 10px; width: 1180px; height: 849px;
    border: 1px solid var(--backdrop-edge);
  }
  .sheet {
    position: absolute; background: var(--paper);
    box-shadow: 0 1px 3px rgba(0,0,0,.18);
  }
  .brand-name {
    position: absolute; color: var(--brand); font-weight: 600;
    letter-spacing: .5px; white-space: nowrap;
  }
  .band {
    position: absolute; background: var(--navy); color: #fff;
    font-size: 9px; line-height: 14px; padding: 0 8px; white-space: nowrap;
  }

  /* Letterhead */
  .letterhead { left: 74px; top: 72px; width: 495px; height: 720px; }
  .letterhead .brand-name { left: 18px; top: 30px; font-size: 26px; }
  .letterhead .tagline { position: absolute; left: 20px; top: 66px; font-size: 7px; color: var(--muted); letter-spacing: 1px; }
  .letterhead .address-line { position: absolute; left: 222px; top: 26px; font-size: 10px; color: var(--navy); white-space: nowrap; }
  .letterhead .email-band { left: 220px; top: 40px; width: 275px; font-size: 9px; }
  .letterhead .figure { position: absolute; left: 236px; top: 372px; width: 140px; height: 312px; }
  .letterhead .web-band { left: 0; top: 682px; width: 495px; height: 14px; }

  /* Envelope front */
  .envelope-front { left: 595px; top: 72px; width: 583px; height: 274px; }
  .envelope-front .brand-name { left: 24px; top: 26px; font-size: 24px; }
  .envelope-front .tagline { position: absolute; left: 26px; top: 60px; font-size: 7px; color: var(--muted); letter-spacing: 1px; }
  .envelope-front .return-band { left: 24px; top: 238px; width: 535px; font-size: 9px; }

  /* Envelope back */
  .envelope-back { left: 595px; top: 355px; width: 583px; height: 259px; }
  .envelope-back svg { position: absolute; left: 0; top: 0; }
  .envelope-back .brand-name { left: 0; width: 583px; text-align: center; top: 100px; font-size: 22px; }

  /* Business card */
  .business-card { left: 595px; top: 629px; width: 214px; height: 134px; }
  .business-card .web-band { left: 50px; top: 12px; width: 164px; font-size: 7px; line-height: 10px; }
  .business-card .brand-name { left: 12px; top: 30px; font-size: 13px; }
  .business-card .holder { position: absolute; left: 118px; top: 32px; }
  .business-card .holder-name { font-size: 10px; color: var(--navy); letter-spacing: 1px; }
  .business-card .holder-title { font-size: 5.5px; color: var(--muted); margin-bottom: 6px; }
  .business-card .contact { font-size: 5.5px; color: var(--muted); line-height: 8px; }
  .business-card .card-address { position: absolute; left: 12px; top: 104px; font-size: 5px; color: var(--muted); white-space: nowrap; }
  .business-card .email-band { left: 0; top: 116px; width: 120px; font-size: 5.5px; line-height: 9px; padding: 0 12px; }
</style>
</head>
<body>
<main class="stage">

  <section class="sheet letterhead" aria-label="Letterhead">
    <div class="brand-name">ALDER GROVE</div>
    <div class="tagline">ALDER GROVE IMAGING</div>
    <div class="address-line">4410 Harbor Line Rd., Suite 210, Fairhaven, TX 70123</div>
    <div class="band email-band">e-mail: tessa@aldergroveimaging.com</div>
    <div class="figure" role="img" aria-label="Illustration of a standing human figure encircled by blue scanning rings"
         style="background: radial-gradient(ellipse at 50% 45%, var(--figure-b) 0%, var(--figure-a) 55%, transparent 75%);"></div>
    <div class="band web-band">www.aldergroveimaging.com</div>
  </section>

  <section class="sheet envelope-front" aria-label="Envelope front">
    <div class="brand-name">ALDER GROVE</div>
    <div class="tagline">ALDER GROVE IMAGING</div>
    <div class="band return-band">4410 Harbor Line Rd., Suite 210, Fairhaven, TX 70123</div>
  </section>

  <section class="sheet envelope-back" aria-label="Envelope back">
    <svg width="583" height="259" viewBox="0 0 583 259" aria-hidden="true">
      <path d="M0 20 H583 M0 20 C150 20 200 150 291.5 150 C383 150 433 20 583 20"
            fill="none" stroke="var(--paper-line)" stroke-width="1"/>
    </svg>
    <div class="brand-name">ALDER GROVE</div>
  </section>

  <section class="sheet business-card" aria-label="Business card">
    <div class="band web-band">www.aldergroveimaging.com</div>
    <div class="brand-name">ALDER GROVE</div>
    <div class="holder">
      <div class="holder-name">TESSA WILDE</div>
      <div class="holder-title">Practice Director</div>
      <div class="contact">Toll Free: 800.555.0142</div>
      <div class="contact">Phone: 210.555.0187</div>
      <div class="contact">Cell: 210.555.0163</div>
      <div class="contact">Fax: 210.555.0190</div>
    </div>
    <div class="card-address">4410 Harbor Line Rd., Suite 210, Fairhaven, TX 70123</div>
    <div class="band email-band">tessa@aldergroveimaging.com</div>
  </section>

</main>
</body>
</html>
```